Real Estate Investor needs awesome business card design

I invest in real estate, focused on multi-family properties, and I need a business card to hand out to potential partners. I prefer simple, clean designs, but it needs to stand out, so I'd like there to be a bit of red in the design as well.

It should include this information:

Front
Dallin Pecksworth
Real Estate Investor
Direct phone: 502-867-3394
Email: dallinhpecksworth@quillmail.example
Headshot (Picture), I've uploaded a few, just pick the one you think looks best with your design. You can remove the background from the headshot image if it looks better.

Back
The back of the card's design should flow and be congruent with the front. On the back I want to put an inspirational quote or question. There will be different ones depending on the card, so I'll need the original file so I can edit it in the end.

For now, use “The Pessimist Sees Difficulty In Every Opportunity. The Optimist Sees The Opportunity In Every Difficulty.” -Barnaby Ellsworth

Target Market(s)

Investors

Industry/Entity Type

Real Estate

Contact Information for Business Card

Front
Dallin Pecksworth
Real Estate Investor

Back
The back of the card's design should flow and be congruent with the front. On the back I want to put an inspirational quote or question. There will be different ones depending on the card, so I'll need the original file so I can edit it in the end. I've uploaded some EXAMPLES of business cards with quotes on them. Don't copy but feel free to use them as inspiration.

The design will be printed on "ZIB sized" business cards
1039 x 697 pixels
with rounded corners

Font styles to use
Serif
Decorative
Script

Colors
ec1f27

Requirements
Must have
• Headshot, name, and other information in it.
• 1039 x 697 pixels
• Rounded corners
• Clean design that pops. I'm open to see any color background, including black.
• Headshots can be located here: https://www.filecrate.example/sh/8kd2wq7mzt31hvx/BBQTXP4ruf9LmQ0KhcvWx7b?dl=0
Nice to have
• It would be awesome if the design included a personal signature or monogram, but if not I'll get a personal logo developed later and the card redesigned if I think it needs it.
Should not have
• Cluttered design

```html
<!DOCTYPE html>
<html lang="en">
<head>
<meta charset="utf-8">
<title>Dallin Pecksworth – Business Card</title>
<link href="https://fonts.googleapis.com/css2?family=Rajdhani:wght@300;400;700&display=swap" rel="stylesheet">
<style>
  :root {
    --brand-red: #ee2150;
    --ink: #3b3b3b;
    --paper: #ffffff;
    --portrait-light: #f1ece9;
    --portrait-skin: #d9a58e;
    --portrait-suit: #1c2236;
  }
  html, body {
    margin: 0;
    padding: 0;
    width: 1200px;
    height: 805px;
    overflow: hidden;
    background: var(--paper);
  }
  .card {
    position: relative;
    width: 1200px;
    height: 805px;
    background: var(--paper);
    overflow: hidden;
    font-family: "Rajdhani", sans-serif;
    color: var(--ink);
  }
  .portrait {
    position: absolute;
    left: 760px;
    top: 0;
    width: 440px;
    height: 805px;
    background: linear-gradient(180deg,
      var(--portrait-light) 0%,
      var(--portrait-skin) 30%,
      var(--portrait-skin) 60%,
      var(--portrait-suit) 82%,
      var(--portrait-suit) 100%);
  }
  .identity {
    position: absolute;
    left: 50px;
    top: 82px;
  }
  .identity__name {
    margin: 0;
    font-weight: 700;
    font-size: 74px;
    line-height: 1;
    letter-spacing: 1px;
    text-transform: uppercase;
    color: var(--brand-red);
  }
  .identity__role {
    margin: 10px 0 0 12px;
    font-weight: 300;
    font-size: 46px;
    line-height: 1;
    text-transform: uppercase;
    color: var(--ink);
  }
  .contact {
    position: absolute;
    left: 112px;
    top: 385px;
    margin: 0;
    padding: 0;
    list-style: none;
  }
  .contact__item {
    display: flex;
    align-items: center;
    height: 66px;
  }
  .contact__item + .contact__item {
    margin-top: 64px;
  }
  .contact__icon {
    width: 66px;
    height: 66px;
    flex: none;
    fill: var(--brand-red);
  }
  .contact__text {
    margin-left: 41px;
    font-weight: 300;
    color: var(--ink);
    text-transform: uppercase;
  }
  .contact__text--phone { font-size: 50px; }
  .contact__text--email { font-size: 27px; letter-spacing: 0.3px; }
</style>
</head>
<body>
  <main class="card">
    <div class="portrait" role="img" aria-label="Headshot of Dallin Pecksworth in a navy suit and white shirt"></div>

    <header class="identity">
      <h1 class="identity__name">Dallin Pecksworth</h1>
      <p class="identity__role">Real Estate Investor</p>
    </header>

    <ul class="contact">
      <li class="contact__item">
        <svg class="contact__icon" viewBox="0 0 24 24" aria-hidden="true">
          <path d="M6.6 10.8c1.4 2.8 3.8 5.1 6.6 6.6l2.2-2.2c.3-.3.7-.4 1-.2 1.1.4 2.3.6 3.6.6.6 0 1 .4 1 1V20c0 .6-.4 1-1 1C10.6 21 3 13.4 3 4c0-.6.4-1 1-1h3.5c.6 0 1 .4 1 1 0 1.3.2 2.5.6 3.6.1.3 0 .7-.2 1L6.6 10.8z"/>
        </svg>
        <span class="contact__text contact__text--phone">502-867-3394</span>
      </li>
      <li class="contact__item">
        <svg class="contact__icon" viewBox="0 0 24 24" aria-hidden="true">
          <path d="M1 5h22v1.2l-11 7.2L1 6.2z"/>
          <path d="M1 8.3l7.4 4.8L1 19.2zM23 8.3v10.9l-7.4-6.1zM9.8 14l2.2 1.4 2.2-1.4 7.6 6H2.2z"/>
        </svg>
        <span class="contact__text contact__text--email">dallinhpecksworth@quillmail.example</span>
      </li>
    </ul>
  </main>
</body>
</html>
```